Landscape Construction and Design Company

We are a landscape construction and design company from New Jersey. We design and install landscapes and hardscapes for residential properties. The name of the company is Brevin's Landscape and Design LLC. We specialize mostly in planting trees and stone work, some water features. We would like to see design themes that include a tree or trees and a stone walkway or wall. We like earth tone colors. We like traditional to modern designs.

Target Market(s)

Homeowners

Industry/Entity Type

Landscape

Contact Information for Business Card

Nature themed design, earth tone colors, space for company name, address, phone numbers, email and website address

Logo Text

No text

Font styles to use
Serif

Colors

Designer to choose colors to be used in the design.

Requirements
Must have
• A tree or trees, similar to the ones uploaded in my supporting images
Nice to have
• I like trees similar to those in my uploaded supporting images. I like artistic, nature theme, earth tone colors
Should not have
• Pictures of real landscapes, cartoon looking logo or objects

```html
<!DOCTYPE html>
<html lang="en">
<head>
<meta charset="utf-8">
<title>Brevin's Landscape &amp; Design LLC — Business Card</title>
<link rel="stylesheet" href="https://fonts.googleapis.com/css2?family=Open+Sans:wght@400;600;700&family=Open+Sans+Condensed:wght@700&display=swap">
<style>
  :root {
    --page-bg: #ece8e2;
    --bark: #4b3029;
    --bark-deep: #3f2822;
    --leaf: #8dc63f;
    --leaf-dark: #6ea82c;
    --sky: #bfe3f2;
    --mist: #eef6ea;
    --meadow: #dff0cf;
    --cream: #f6f1e6;
    --white: #ffffff;
  }
  * { margin: 0; padding: 0; box-sizing: border-box; }
  html, body { width: 1200px; height: 1000px; overflow: hidden; }
  body {
    background: var(--page-bg);
    font-family: "Open Sans", Arial, sans-serif;
    position: relative;
  }
  .card {
    position: absolute;
    left: 250px;
    width: 700px;
    height: 400px;
    overflow: hidden;
    box-shadow: 0 6px 18px rgba(0,0,0,0.22);
  }
  .card--front { top: 70px; }
  .card--back { top: 530px; background: var(--bark); }

  .front__wash {
    position: absolute; inset: 0;
    background:
      radial-gradient(ellipse at 30% 70%, var(--meadow) 0%, transparent 55%),
      radial-gradient(ellipse at 75% 40%, var(--mist) 0%, transparent 60%),
      linear-gradient(170deg, var(--sky) 0%, #d6eef2 45%, var(--mist) 100%);
  }
  .front__bands { position: absolute; inset: 0; }

  .brand-name {
    position: absolute;
    font-family: "Open Sans", Arial, sans-serif;
    font-weight: 700;
    color: var(--bark);
    text-align: center;
    line-height: 1.15;
  }
  .card--front .brand-name {
    left: 40px; top: 105px; width: 200px;
    font-size: 22px;
  }

  .person { position: absolute; right: 40px; top: 48px; text-align: right; }
  .person__name {
    font-family: "Open Sans Condensed", "Open Sans", Arial, sans-serif;
    font-weight: 700;
    font-size: 30px;
    color: var(--bark);
    letter-spacing: 0.5px;
  }
  .person__role {
    font-weight: 600;
    font-size: 18px;
    color: var(--leaf);
    margin-top: 2px;
  }

  .contacts {
    position: absolute; right: 22px; top: 222px;
    list-style: none;
    color: var(--white);
    font-size: 16px;
    text-align: right;
  }
  .contacts li {
    display: flex; justify-content: flex-end; align-items: center;
    height: 21px;
  }
  .contacts li.gap { margin-top: 11px; }
  .contacts .icon { width: 15px; height: 15px; margin-left: 9px; }
  .contacts .icon--blank { visibility: hidden; }

  .card--back .brand-name {
    left: 200px; top: 160px; width: 300px;
    font-size: 26px;
    color: var(--cream);
  }
</style>
</head>
<body>

<section class="card card--front" aria-label="Business card front">
  <div class="front__wash" role="img" aria-label="Soft watercolour sky wash in blue and pale green"></div>
  <svg class="front__bands" viewBox="0 0 700 400" width="700" height="400" aria-hidden="true">
    <path d="M0,318 C140,350 330,330 480,262 C390,318 200,352 0,338 Z" fill="var(--leaf)"/>
    <path d="M0,345 C170,362 380,300 520,222 C580,195 640,185 700,183 L700,400 L0,400 Z" fill="var(--bark)"/>
  </svg>

  <p class="brand-name">Brevin's Landscape<br>&amp; Design LLC</p>

  <div class="person">
    <p class="person__name">PERSON'S NAME</p>
    <p class="person__role">FOUNDER</p>
  </div>

  <ul class="contacts">
    <li>0123-456-7890
      <svg class="icon" viewBox="0 0 16 16"><circle cx="8" cy="8" r="7.5" fill="none" stroke="#fff" stroke-width="1"/><path d="M5 4.5l1.6-.3 1 2-1 .8c.5 1.1 1.3 1.9 2.4 2.4l.8-1 2 1-.3 1.6C8 11.2 4.8 8 5 4.5z" fill="#fff"/></svg>
    </li>
    <li>0123-456-7890
      <svg class="icon icon--blank" viewBox="0 0 16 16"></svg>
    </li>
    <li class="gap">yourname@domain.com
      <svg class="icon" viewBox="0 0 16 16"><circle cx="8" cy="8" r="7.5" fill="none" stroke="#fff" stroke-width="1"/><rect x="4" y="5.3" width="8" height="5.4" fill="#fff"/><path d="M4 5.3l4 3 4-3" fill="none" stroke="var(--bark)" stroke-width="0.9"/></svg>
    </li>
    <li class="gap">www.yoursite.com
      <svg class="icon" viewBox="0 0 16 16"><circle cx="8" cy="8" r="7.5" fill="none" stroke="#fff" stroke-width="1"/><circle cx="8" cy="8" r="4" fill="none" stroke="#fff" stroke-width="1"/><path d="M4 8h8M8 4c-1.6 2.2-1.6 5.8 0 8M8 4c1.6 2.2 1.6 5.8 0 8" fill="none" stroke="#fff" stroke-width="0.8"/></svg>
    </li>
    <li class="gap">Your Address goes here
      <svg class="icon" viewBox="0 0 16 16"><circle cx="8" cy="8" r="7.5" fill="none" stroke="#fff" stroke-width="1"/><path d="M8 4.2l4 3.4h-1.1v4H5.1v-4H4z" fill="#fff"/><rect x="7.2" y="9" width="1.6" height="2.6" fill="var(--bark)"/></svg>
    </li>
  </ul>
</section>

<section class="card card--back" aria-label="Business card back">
  <p class="brand-name">Brevin's Landscape<br>&amp; Design LLC</p>
</section>

</body>
</html>
```